Tequila Startup Company Booklet Design

Need a 16 or so page booklet for a spirits company (like tequila) artfully designed. Need a killer design and beautifully and thoughtfully laid out in a compelling manner. Need talented and creative designer to craft an eye catching booklet.
Updates

Low designer entries

Target Market(s)

Investors and tequila drinkers

Industry/Entity Type

Alcohol spirits distillery

Colors

Designer to choose colors to be used in the design.

Requirements
Must have
• Beautiful graphics and photos relevant to agave fields
Nice to have
• Want to emphasize the blue agave fields and the distillery process

```html
<!DOCTYPE html>
<html lang="en">
<head>
<meta charset="UTF-8">
<title>Heart of the Highlands – Booklet Spread</title>
<link href="https://fonts.googleapis.com/css2?family=Playfair+Display:wght@400;500&family=Mulish:ital,wght@0,400;0,500;1,500&display=swap" rel="stylesheet">
<style>
  :root {
    --backdrop: #d2d2d2;
    --paper: #eeeeee;
    --paper-right: #ececec;
    --ink: #2b2b2b;
    --gold: #c2a574;
    --gold-deep: #b39666;
    --gold-text: #c09a5e;
    --agave-teal: #2f7d80;
    --agave-blue: #6f9bb3;
    --map-sand: #d8c9a3;
    --map-highland: #a8956a;
  }
  * { margin: 0; padding: 0; box-sizing: border-box; }
  html, body {
    width: 1200px; height: 800px; overflow: hidden;
    background: var(--backdrop);
  }
  .spread {
    position: absolute; left: 40px; top: 20px;
    width: 1120px; height: 760px;
    display: flex;
    box-shadow: 0 6px 18px rgba(0,0,0,0.15);
  }
  .page {
    position: relative; width: 560px; height: 760px;
    background: var(--paper);
    color: var(--ink);
    font-family: "Mulish", sans-serif;
  }
  .page--left {
    background: linear-gradient(to right, var(--paper) 88%, #e2e2e2 100%);
  }
  .page--right {
    background: linear-gradient(to left, var(--paper-right) 92%, #e4e4e4 100%);
  }
  .page-title {
    position: absolute; left: 0; right: 0;
    text-align: center;
    font-family: "Playfair Display", serif;
    font-weight: 500;
    font-size: 37px;
    line-height: 1.12;
    letter-spacing: 0.1em;
    text-transform: uppercase;
  }
  .page-title .small { font-size: 0.8em; }
  .page--left .page-title { top: 44px; }
  .page--right .page-title { top: 46px; }

  .agave-illustration {
    position: absolute; left: 140px; top: 137px;
    width: 290px; height: 200px;
    background: radial-gradient(ellipse at 50% 85%, var(--agave-blue) 0%, var(--agave-teal) 45%, rgba(47,125,128,0.0) 72%);
  }
  .species-caption {
    position: absolute; left: 0; right: 0; top: 352px;
    text-align: center;
    font-style: italic; font-weight: 500;
    font-size: 24px;
    color: var(--gold-text);
    letter-spacing: 0.02em;
  }
  .feature-band {
    position: absolute; left: 67px; right: 58px; top: 405px;
    height: 72px;
    background: linear-gradient(to right, var(--gold-deep), var(--gold) 60%, #c9ae82);
    display: flex; flex-direction: column; justify-content: center;
    text-align: center;
    font-size: 17.5px; line-height: 1.7;
    color: var(--ink);
  }
  .body-copy {
    position: absolute;
    font-size: 14.6px; line-height: 1.6;
    color: var(--ink);
  }
  .page--left .body-copy { left: 65px; right: 62px; }
  .page--right .body-copy { left: 63px; right: 60px; }

  .jalisco-map {
    position: absolute; left: 146px; top: 198px;
    width: 240px; height: 264px;
  }
</style>
</head>
<body>
  <main class="spread">
    <section class="page page--left">
      <h1 class="page-title">Heart <span class="small">of</span><br>The Highlands</h1>
      <div class="agave-illustration" role="img" aria-label="Watercolour illustration of a blue agave plant"></div>
      <p class="species-caption">Agave tequilana</p>
      <div class="feature-band">
        <span>Only 100% Blue Weber Agave</span>
        <span>Minimum 7-Year Maturation</span>
      </div>
      <p class="body-copy" style="top:510px;">We proudly use only the Blue Weber variety of agave, prized for its high sugar content and exceptional quality.</p>
      <p class="body-copy" style="top:576px;">Cultivated in the Jalisco Highlands, the rich, red volcanic soil and elevation provide perfect conditions for agave to flourish.</p>
      <p class="body-copy" style="top:666px;">Our maturation process begins in the fields and continues through slow, natural growth cycles — never rushed.</p>
    </section>

    <section class="page page--right">
      <h2 class="page-title">Sourcing From<br>The Highlands <span class="small">of</span><br>Jalisco</h2>
      <svg class="jalisco-map" viewBox="0 0 240 264" role="img" aria-label="Map of Jalisco with the Highlands region highlighted among neighbouring states">
        <rect x="0" y="0" width="240" height="264" rx="40" fill="var(--map-sand)"/>
        <ellipse cx="75" cy="140" rx="34" ry="26" fill="var(--map-highland)"/>
      </svg>
      <p class="body-copy" style="top:508px;">Our agave fields thrive in the Jalisco Highlands — a region renowned for its ideal climate, high elevation, and rich, iron-oxide soil.</p>
      <p class="body-copy" style="top:598px;">This unique terroir imparts a distinct character to our tequila, reflecting the land from which it is born.</p>
      <p class="body-copy" style="top:666px;">We work directly with small, multi-generational growers who cultivate with reverence for both tradition and land.</p>
    </section>
  </main>
</body>
</html>
```